Velmorak720 is a marketing advisory service company. We provide the following services:
Marketing Strategy
PR and Marketing Communication
Field Marketing
Digital Marketing

We would like to see a design that has either of the following copy:

Everyone can develop a product for the market; not everyone can access the market with the product. Let Velmorak720 help you access the market profitably.

or

Almost every business know how to create value, nor every business can capture value. At Velmorak720, we specialize in helping businesses capture value.

or

It is easy to start a business, attracting and retaining customers and client is the real work. At Velmorak720, we specialize in helping our businesses attract and retain customers and clients.

We can have a slogan that reads:

V-720, your market development partner.....

```html
<!DOCTYPE html>
<html lang="en">
<head>
<meta charset="utf-8">
<title>Velmorak720 – Banner Set</title>
<link href="https://fonts.googleapis.com/css2?family=Open+Sans:wght@600;700&display=swap" rel="stylesheet">
<style>
  :root {
    --brand-blue: #0b4f9c;
    --deep-blue: #0a4890;
    --brand-yellow: #fff000;
    --accent-yellow: #ffeb00;
    --slogan-blue: #1657a8;
    --chart-blue: rgba(26, 95, 180, 0.55);
    --chart-yellow: rgba(255, 236, 0, 0.9);
    --white: #ffffff;
    --page: #ffffff;
  }
  * { margin: 0; padding: 0; box-sizing: border-box; }
  html, body { width: 1200px; height: 1000px; overflow: hidden; background: var(--page); }
  body { position: relative; font-family: "Open Sans", Arial, sans-serif; }

  .banner { position: absolute; overflow: hidden; }
  .banner > * { position: absolute; }

  .banner--skyscraper { left: 103px; top: 144px; width: 160px; height: 600px;
    background: linear-gradient(to bottom, var(--brand-blue) 0%, var(--brand-blue) 55%, var(--brand-yellow) 92%); }
  .banner--rectangle { left: 303px; top: 89px; width: 336px; height: 280px;
    background: linear-gradient(to bottom, var(--brand-blue) 0%, var(--brand-blue) 35%, var(--brand-yellow) 90%); }
  .banner--medium { left: 707px; top: 119px; width: 300px; height: 250px;
    background: linear-gradient(to bottom, var(--brand-blue) 0%, var(--brand-blue) 35%, var(--brand-yellow) 90%); }
  .banner--leaderboard { left: 303px; top: 404px; width: 728px; height: 90px;
    background: linear-gradient(to right, var(--brand-blue) 0%, var(--brand-blue) 55%, var(--brand-yellow) 90%); }
  .banner--billboard { left: 303px; top: 524px; width: 646px; height: 220px;
    background: linear-gradient(to right, var(--brand-blue) 0%, var(--deep-blue) 38%, var(--brand-yellow) 90%); }

  .brand-name { color: var(--white); font-weight: 600; white-space: nowrap; text-align: center; }

  .headline { color: var(--white); font-weight: 600; text-align: center; text-transform: uppercase; }
  .headline .hl { color: var(--accent-yellow); }
  .headline strong { font-weight: 700; }

  .slogan { color: var(--slogan-blue); font-weight: 700; text-align: center; }

  .growth-visual { border-radius: 4px;
    background: linear-gradient(to top right, var(--chart-blue) 0%, var(--chart-yellow) 70%); }
</style>
</head>
<body>

<!-- Skyscraper 160 x 600 -->
<section class="banner banner--skyscraper">
  <span class="brand-name" style="left:0;top:108px;width:160px;font-size:20px">Velmorak720</span>
  <p class="headline" style="left:0;top:150px;width:160px;font-size:13.5px;line-height:17.5px">
    Everyone<br><span class="hl">can develop<br>a product</span><br>for the market;<br>not everyone<br><span class="hl">can access<br>the market</span><br>with the product.<br><strong>Let Velmorak720</strong><br><span class="hl">help you access<br>the market<br>profitably.</span>
  </p>
  <div class="growth-visual" role="img" aria-label="Growth bar chart illustration with rising arrow" style="left:27px;top:361px;width:120px;height:120px"></div>
  <p class="slogan" style="left:0;top:508px;width:160px;font-size:15px;line-height:20px">V-720, your<br>market<br>development<br>partner</p>
</section>

<!-- Rectangle 336 x 280 -->
<section class="banner banner--rectangle">
  <span class="brand-name" style="left:4px;top:80px;width:104px;font-size:15px">Velmorak720</span>
  <p class="headline" style="left:114px;top:5px;width:220px;font-size:12.5px;line-height:16px">
    Everyone <span class="hl">can develop<br>a product</span> for the market;<br>not everyone <span class="hl">can access<br>the market</span> with the product.<br><strong>Let Velmorak720</strong><br><span class="hl">help you access<br>the market profitably.</span>
  </p>
  <div class="growth-visual" role="img" aria-label="Growth bar chart illustration with rising arrow" style="left:30px;top:148px;width:122px;height:118px"></div>
  <p class="slogan" style="left:192px;top:188px;width:130px;font-size:16px;line-height:19px">V-720, your<br>market<br>development<br>partner</p>
</section>

<!-- Medium rectangle 300 x 250 -->
<section class="banner banner--medium">
  <span class="brand-name" style="left:2px;top:70px;width:96px;font-size:14px">Velmorak720</span>
  <p class="headline" style="left:98px;top:4px;width:200px;font-size:11.5px;line-height:14.6px">
    Everyone <span class="hl">can develop<br>a product</span> for the market;<br>not everyone <span class="hl">can access<br>the market</span> with the product.<br><strong>Let Velmorak720</strong><br><span class="hl">help you access<br>the market profitably.</span>
  </p>
  <div class="growth-visual" role="img" aria-label="Growth bar chart illustration with rising arrow" style="left:26px;top:129px;width:110px;height:108px"></div>
  <p class="slogan" style="left:150px;top:167px;width:130px;font-size:15px;line-height:17.5px">V-720, your<br>market<br>development<br>partner</p>
</section>

<!-- Leaderboard 728 x 90 -->
<section class="banner banner--leaderboard">
  <span class="brand-name" style="left:4px;top:70px;width:94px;font-size:14px">Velmorak720</span>
  <p class="headline" style="left:100px;top:12px;width:440px;font-size:12.2px;line-height:21px">
    Everyone <span class="hl">can develop a product</span> for the market;<br>not everyone <span class="hl">can access the market</span> with the product.<br><strong>Let Velmorak720</strong> <span class="hl">help you access the market profitably.</span>
  </p>
  <div class="growth-visual" role="img" aria-label="Growth bar chart illustration with rising arrow" style="left:547px;top:4px;width:80px;height:80px"></div>
  <p class="slogan" style="left:630px;top:15px;width:92px;font-size:11px;line-height:14px">V-720, your<br>market<br>development<br>partner</p>
</section>

<!-- Billboard 646 x 220 -->
<section class="banner banner--billboard">
  <span class="brand-name" style="left:4px;top:146px;width:126px;font-size:19px">Velmorak720</span>
  <p class="headline" style="left:120px;top:18px;width:376px;font-size:18px;line-height:23.6px">
    Everyone <span class="hl">can develop<br>a product</span> for the market;<br>not everyone <span class="hl">can access<br>the market</span> with the product.<br><strong>Let Velmorak720</strong><br><span class="hl">help you access<br>the market profitably.</span>
  </p>
  <p class="slogan" style="left:490px;top:4px;width:136px;font-size:16px;line-height:19px">V-720, your<br>market<br>development<br>partner</p>
  <div class="growth-visual" role="img" aria-label="Growth bar chart illustration with rising arrow" style="left:482px;top:106px;width:112px;height:100px"></div>
</section>

</body>
</html>
```